Copper and Slate Mists NZ new website!

We are a new online vaping retailer and are looking for an awesome sleek website. We are going to be selling a variety of vaping products and gear. Our logo has just been developed and we would like to keep the website in line with the black, tan a white theme. We would like to trying watermarking or imposing the rottie into the background of the website on the home page, with the page being black and you can see the tan and white colours only.

Coding

Coded - Design and coding required

Number of Pages Required

2 page

Font styles to use
Serif
Sans Serif
Decorative

Requirements
Must have
• A home page and a standard page for products
• Stay in line with the colours in the logo

```html
<!DOCTYPE html>
<html lang="en">
<head>
<meta charset="utf-8">
<title>Copper and Slate Mists NZ — Shop</title>
<link rel="stylesheet" href="https://fonts.googleapis.com/css2?family=Open+Sans:wght@400;600;700;800&family=Bungee+Outline&display=swap">
<style>
:root{
  --black:#000;
  --ink:#0a0a0a;
  --tan:#e3a24c;
  --tan-soft:#eaae63;
  --tan-dark:#8b5a22;
  --white:#fff;
  --grey:#cfcfcf;
  --grey-mid:#9a9a9a;
  --line:#2a2a2a;
}
*{box-sizing:border-box;margin:0;padding:0}
html,body{width:1200px;height:3219px;overflow:hidden;background:var(--black);font-family:"Open Sans",Arial,sans-serif;color:var(--white)}
.page{position:relative;width:1200px;height:3219px}
.abs{position:absolute}

/* hero */
.hero{left:0;top:0;width:1200px;height:775px;background:radial-gradient(ellipse at 30% 35%,#6a6a6a 0%,#3a3a3a 35%,#1c1c1c 70%,#0e0e0e 100%)}
.brand{left:520px;top:34px;width:160px;text-align:center}
.brand-dot{width:70px;height:70px;border-radius:50%;background:var(--tan);margin:0 auto 8px}
.brand-name{font-weight:700;font-size:13px;color:var(--tan);letter-spacing:.5px;line-height:1.25}
.nav-home{left:943px;top:45px;width:170px;height:55px;border:2px solid var(--white);font-weight:600;font-size:25px;letter-spacing:1px;display:flex;align-items:center;justify-content:center}
.hero-title{left:760px;top:232px;width:355px;text-align:right;font-weight:800;font-size:104px;color:var(--tan);line-height:1.1;letter-spacing:1px}
.hero-text{left:850px;top:372px;width:265px;text-align:right;font-size:14.5px;line-height:20px;color:var(--grey)}

/* welcome */
.welcome{left:0;top:876px;width:1200px;text-align:center;font-weight:700;font-size:38px;color:#d4d4d4;letter-spacing:.5px}
.welcome-rule{left:505px;top:932px;width:190px;height:3px;background:var(--tan)}

/* sidebar */
.panel{border:1.5px solid var(--tan-dark)}
.cart{left:121px;top:1029px;width:300px;height:712px;padding:0 21px}
.panel-title{font-weight:700;font-size:15px;letter-spacing:.3px}
.cart .t1{margin-top:22px}
.cart-empty{font-size:9px;color:var(--grey);margin-top:14px;letter-spacing:.3px}
.cart-note{font-size:10.5px;line-height:14px;color:var(--grey);margin-top:10px;width:230px}
.divider{height:1px;background:#555;margin-top:30px}
.cat-title{margin-top:30px}
.cats{list-style:none;margin-top:23px;font-size:13px;line-height:20px;color:var(--grey)}
.cats li{position:relative;padding-left:17px}
.cats li.top::before{content:"";position:absolute;left:0;top:6px;border-left:7px solid var(--tan);border-top:4px solid transparent;border-bottom:4px solid transparent}
.cats li.sub{padding-left:37px}
.cats li.sub.active{font-weight:700;color:var(--white)}
.cats li.sub.active::before{content:"";position:absolute;left:23px;top:6px;border-left:7px solid var(--tan);border-top:4px solid transparent;border-bottom:4px solid transparent}
.cart .divider.low{margin-top:22px}
.cart-foot{font-size:10.5px;line-height:14px;color:#888;margin-top:12px}

.sale{left:121px;top:1765px;width:300px;height:866px}
.sale-title{left:36px;top:26px;font-family:"Bungee Outline",Impact,sans-serif;font-size:88px;line-height:84px;color:var(--tan)}
.sale-text{left:36px;top:218px;width:145px;font-size:12px;line-height:15.5px;color:var(--grey)}
.sale-device{left:190px;top:218px;width:70px;height:195px;border-radius:10px;background:linear-gradient(90deg,#bfbfbf,#f4f4f4 40%,#2a2a2a 55%,#111)}
.sale-photo{left:36px;top:415px;width:235px;height:445px;background:radial-gradient(ellipse at 50% 45%,#c27a2a 0%,#6d4316 45%,#1a1208 80%,#000 100%)}

/* products */
.results{left:465px;top:1063px;font-size:9px;letter-spacing:.3px;color:var(--grey)}
.sort{left:882px;top:1032px;width:208px;height:45px;background:var(--tan);color:var(--black);font-weight:700;font-size:12.5px;display:flex;align-items:center;justify-content:space-between;padding:0 14px}
.card{width:300px;height:363px;background:var(--white);color:var(--black)}
.card-img{position:absolute;left:110px;top:42px;width:80px;height:172px;border-radius:8px;background:linear-gradient(90deg,#b9b9b9,#f5f5f5 38%,#2b2b2b 52%,#0f0f0f)}
.card-price{position:absolute;left:0;top:253px;width:100%;text-align:center;font-weight:700;font-size:26px;color:#222}
.card-name{position:absolute;left:0;top:292px;width:100%;text-align:center;font-size:10px;letter-spacing:.4px;color:#444}
.card-btn{position:absolute;left:81px;top:318px;width:138px;height:27px;background:var(--tan-soft);color:var(--white);font-weight:700;font-size:11px;display:flex;align-items:center;justify-content:center}

.pager{left:620px;top:2686px;display:flex;gap:12px;align-items:center;font-size:15px;font-weight:600}
.pager .current{border:2px solid var(--tan);width:28px;height:28px;display:flex;align-items:center;justify-content:center;color:var(--white)}
.pager span{color:var(--tan)}

/* footer */
.footer-rule{left:0;top:2805px;width:1200px;height:1px;background:var(--line)}
.to-top{left:1130px;top:2795px;width:36px;height:36px;background:var(--tan);display:flex;align-items:center;justify-content:center}
.foot-brand{left:79px;top:2880px;width:160px;text-align:center}
.foot-brand .brand-dot{width:110px;height:110px}
.foot-head{font-weight:700;font-size:16px;color:var(--tan);letter-spacing:.4px}
.foot-col{top:2898px}
.foot-list{list-style:none;margin-top:22px;font-size:10px;line-height:20px;color:var(--grey);letter-spacing:.3px}
.col-info{left:310px}
.col-news{left:520px;width:240px}
.col-contact{left:825px;width:190px}
.news-text{font-size:10.5px;line-height:14px;color:var(--grey);margin-top:22px}
.news-input{margin-top:14px;width:232px;height:24px;border:1px solid #777;font-size:9px;color:#aaa;padding:6px 8px}
.news-hint{font-size:8.5px;color:#888;margin-top:5px}
.news-btn{margin-top:10px;width:92px;height:24px;background:var(--tan);color:var(--black);font-weight:700;font-size:10px;display:flex;align-items:center;justify-content:center}
.news-terms{font-size:8.5px;color:#888;margin-top:10px}
.contact-text{font-size:10px;line-height:13px;color:var(--grey);margin-top:22px}
.contact-line{font-size:10px;color:var(--tan);margin-top:14px}
.contact-line + .contact-line{margin-top:6px}
.follow{font-size:10px;font-weight:700;color:var(--grey);margin-top:20px;letter-spacing:.5px}
.socials{display:flex;gap:14px;margin-top:14px}
.socials i{display:block;width:18px;height:18px;border-radius:50%;background:var(--tan)}
</style>
</head>
<body>
<div class="page">

  <header>
    <div class="abs hero" role="img" aria-label="Black and white photograph of two rottweiler dogs sitting on a porch"></div>
    <div class="abs brand">
      <div class="brand-dot"></div>
      <div class="brand-name">Copper &amp; Slate Mists NZ</div>
    </div>
    <div class="abs nav-home">HOME</div>
    <h1 class="abs hero-title">SHOP</h1>
    <p class="abs hero-text">Lorem ipsum dolor sit amet, consectetuer adipiscing elit, sed diam nonummy nibh euismod tincidunt ut laoreet dolore magna aliquam erat volutpat. Ut wisi enim ad minim veniam, quis nostrud exerci tation ullamcorper suscipit lobortis nisl</p>
  </header>

  <h2 class="abs welcome">WELCOME TO OUR SHOP</h2>
  <div class="abs welcome-rule"></div>

  <aside>
    <div class="abs panel cart">
      <div class="panel-title t1">SHOPPING CART</div>
      <div class="cart-empty">NO PRODUCTS SELECTED</div>
      <p class="cart-note">Lorem ipsum dolor sit amet, consectetuer adipiscing elit, sed diam nonummy nibh euis mod tincidunt ut laoreet dolore magna.</p>
      <div class="divider"></div>
      <div class="panel-title cat-title">PRODUCTS CATEGORIES</div>
      <ul class="cats">
        <li class="top">Accesories</li>
        <li class="top">Devices</li>
        <li class="top">E-juices</li>
        <li class="top">Started Kits</li>
        <li class="top">Box-Mods</li>
        <li class="sub active">BOX BRAND 1</li>
        <li class="sub">BOX BRAND 2</li>
        <li class="sub">BOX BRAND 3</li>
        <li class="sub">BOX BRAND 4</li>
        <li class="sub">BOX BRAND 5</li>
        <li class="sub">BOX BRAND 6</li>
        <li class="top">Pen</li>
        <li class="top">Promotion products</li>
        <li class="sub">ITEM 1</li>
        <li class="sub">ITEM 2</li>
        <li class="sub">ITEM 3</li>
        <li class="sub">ITEM 4</li>
        <li class="sub">ITEM 5</li>
      </ul>
      <div class="divider low"></div>
      <p class="cart-foot">Lorem ipsum dolor sit amet, consectetuer adipiscing elit, sed diam nonummy nibh euismod tincidunt ut laoreet dolore magna</p>
    </div>

    <div class="abs panel sale">
      <div class="abs sale-title">ON<br>SALE!</div>
      <p class="abs sale-text">Lorem ipsum dolor sit amet, consectetuer adipiscing elit, sed diam nonummy nibh euismod tincidunt ut laoreet dolore magna aliquam erat volutpat. Ut wisi enim ad minim veniam, quis nostrud exerci tation ullamcorper suscipit lobortis nisl</p>
      <div class="abs sale-device" role="img" aria-label="Box mod vaping device"></div>
      <div class="abs sale-photo" role="img" aria-label="Photograph of a man in a cap blowing a vapour ring, toned in tan"></div>
    </div>
  </aside>

  <main>
    <div class="abs results">SHOWING 1-8 OF 25 RESULTS</div>
    <div class="abs sort">LOW PRICES
      <svg width="12" height="8" viewBox="0 0 12 8"><path d="M1 1l5 5 5-5" fill="none" stroke="#000" stroke-width="2"/></svg>
    </div>

    <div class="abs card" style="left:465px;top:1113px"><div class="card-img" role="img" aria-label="Box mod device"></div><div class="card-price">$99.99</div><div class="card-name">LOREM IMPSUN DOLOR SIT</div><div class="card-btn">MORE</div></div>
    <div class="abs card" style="left:788px;top:1113px"><div class="card-img" role="img" aria-label="Box mod device"></div><div class="card-price">$99.99</div><div class="card-name">LOREM IMPSUN DOLOR SIT</div><div class="card-btn">MORE</div></div>
    <div class="abs card" style="left:465px;top:1497px"><div class="card-img" role="img" aria-label="Box mod device"></div><div class="card-price">$99.99</div><div class="card-name">LOREM IMPSUN DOLOR SIT</div><div class="card-btn">MORE</div></div>
    <div class="abs card" style="left:788px;top:1497px"><div class="card-img" role="img" aria-label="Box mod device"></div><div class="card-price">$99.99</div><div class="card-name">LOREM IMPSUN DOLOR SIT</div><div class="card-btn">MORE</div></div>
    <div class="abs card" style="left:465px;top:1883px"><div class="card-img" role="img" aria-label="Box mod device"></div><div class="card-price">$99.99</div><div class="card-name">LOREM IMPSUN DOLOR SIT</div><div class="card-btn">MORE</div></div>
    <div class="abs card" style="left:788px;top:1883px"><div class="card-img" role="img" aria-label="Box mod device"></div><div class="card-price">$99.99</div><div class="card-name">LOREM IMPSUN DOLOR SIT</div><div class="card-btn">MORE</div></div>
    <div class="abs card" style="left:465px;top:2266px"><div class="card-img" role="img" aria-label="Box mod device"></div><div class="card-price">$99.99</div><div class="card-name">LOREM IMPSUN DOLOR SIT</div><div class="card-btn">MORE</div></div>
    <div class="abs card" style="left:788px;top:2266px"><div class="card-img" role="img" aria-label="Box mod device"></div><div class="card-price">$99.99</div><div class="card-name">LOREM IMPSUN DOLOR SIT</div><div class="card-btn">MORE</div></div>

    <nav class="abs pager">
      <div class="current">1</div><span>2</span><span>3</span><span>&gt;</span><span>&gt;&gt;</span>
    </nav>
  </main>

  <footer>
    <div class="abs footer-rule"></div>
    <div class="abs to-top"><svg width="14" height="9" viewBox="0 0 14 9"><path d="M1 8l6-6 6 6" fill="none" stroke="#fff" stroke-width="2"/></svg></div>
    <div class="abs foot-brand">
      <div class="brand-dot"></div>
      <div class="brand-name">Copper &amp; Slate Mists NZ</div>
    </div>

    <div class="abs foot-col col-info">
      <div class="foot-head">INFORMATION</div>
      <ul class="foot-list">
        <li>ABOUT US</li><li>ACCESSORIES</li><li>DEVICES</li><li>E-JUICES</li><li>STARTER KITS</li><li>PRIVACY POLICY</li><li>FAQ</li><li>SHIPPING</li>
      </ul>
    </div>

    <div class="abs foot-col col-news">
      <div class="foot-head">NEWSLETTER</div>
      <p class="news-text">Stay up to date with all our latest products and promotions</p>
      <div class="news-input">your email...</div>
      <div class="news-hint">I have read and agree to the terms &amp; conditions</div>
      <div class="news-btn">SUBSCRIBE</div>
      <div class="news-terms">Terms &amp; Conditions</div>
    </div>

    <div class="abs foot-col col-contact">
      <div class="foot-head">CONTACT US</div>
      <p class="contact-text">Lorem ipsum dolor sit amet, consectetuer adipiscing elit, sed diam nonummy nibh euismod.</p>
      <div class="contact-line">PHONE: +64 9 555 0142</div>
      <div class="contact-line">hello@copperslatemists.co.nz</div>
      <div class="follow">FOLLOW US ON</div>
      <div class="socials"><i></i><i></i><i></i><i></i></div>
    </div>
  </footer>

</div>
</body>
</html>
```